Design logo and business card.

Design and construct logo and card for my business which is an over seeing company of other smaller businesses. The companies name is quarry5 business collective. Im open to any ideas but i am looking for a very cool contemporary design with a very prestige feel. The card can be either single or double sided, Thank you and i will look forward to your submissions.

Industry/Entity Type

Business

Requirements
Must have
• Company name, email, website, telephone, my name. Cool modern look with a prestige feel.

```html
<!DOCTYPE html>
<html lang="en">
<head>
<meta charset="utf-8">
<title>quarry5 business collective — business card set</title>
<link rel="stylesheet" href="https://fonts.googleapis.com/css2?family=Open+Sans:wght@400;600&display=swap">
<style>
  :root {
    --page: #ffffff;
    --card-dark: #232525;
    --pattern-light: #2f2f2f;
    --pattern-dark: #1c1c1c;
    --gold: #f6c231;
    --gold-soft: #ffe9a6;
    --silver: #c9c9c9;
    --silver-dark: #7d7d7d;
    --white: #ffffff;
    --edge: #555555;
  }
  * { box-sizing: border-box; margin: 0; padding: 0; }
  html, body { width: 1200px; height: 1000px; overflow: hidden; background: var(--page); }
  body { position: relative; font-family: "Open Sans", Arial, sans-serif; }

  .card {
    position: absolute;
    width: 417px;
    height: 241px;
    border-radius: 20px;
    overflow: hidden;
    border: 1px solid var(--edge);
    background: var(--card-dark);
  }
  .card-front { left: 176px; }
  .card-back { left: 611px; width: 418px; }

  .damask-fill {
    position: absolute;
    left: 0; top: 0; width: 100%; height: 100%;
    background:
      radial-gradient(ellipse at 50% 45%, var(--pattern-light) 0%, #262626 55%, var(--pattern-dark) 100%);
  }
  .card-back .damask-fill { height: 125px; }

  /* front */
  .brand-name {
    position: absolute;
    left: 0; width: 100%;
    top: 82px;
    text-align: center;
    line-height: 1;
  }
  .brand-name .wordmark { display: block; font-size: 40px; font-weight: 400; letter-spacing: 1px; }
  .brand-name .tagline { display: block; font-size: 13px; font-weight: 400; margin-top: 4px; }
  .brand-gold { color: var(--gold); }
  .brand-silver { color: var(--silver); }

  .band-long {
    position: absolute; left: 0; top: 206px; width: 244px; height: 8px;
    clip-path: polygon(0 0, 100% 0, 97% 100%, 0 100%);
  }
  .band-short {
    position: absolute; left: 377px; top: 206px; width: 40px; height: 8px;
    clip-path: polygon(8% 0, 100% 0, 100% 100%, 0 100%);
  }
  .web-address {
    position: absolute; left: 254px; top: 201px;
    font-size: 13px; color: var(--white); letter-spacing: 0.2px;
  }
  .web-address.gold { color: var(--gold); }

  .band-gold-glow { background: linear-gradient(90deg, var(--white) 0%, var(--gold-soft) 25%, var(--gold) 60%, var(--gold) 100%); }
  .band-gold-glow-short { background: linear-gradient(90deg, var(--gold), var(--gold-soft) 70%, var(--white)); }
  .band-silver { background: linear-gradient(90deg, #ffffff 0%, var(--silver) 40%, var(--silver-dark) 100%); }
  .band-silver-short { background: linear-gradient(90deg, var(--silver-dark), var(--silver)); }
  .band-gold-flat { background: var(--gold); }

  /* back */
  .company-heading {
    position: absolute; left: 0; width: 100%; top: 83px;
    text-align: center; font-size: 20px; font-weight: 400;
    color: var(--white); letter-spacing: 0.2px;
  }
  .company-heading.gold { color: var(--gold); }
  .divider {
    position: absolute; left: 0; top: 125px; width: 100%; height: 6px;
  }
  .divider-gold-fade { background: linear-gradient(90deg, #ffffff 0%, var(--gold-soft) 15%, var(--gold) 40%, var(--gold) 100%); }
  .divider-silver { background: linear-gradient(90deg, #8a8a8a 0%, #bdbdbd 40%, #ffffff 55%, #a0a0a0 75%, #8a8a8a 100%); }
  .divider-gold-flat { background: var(--gold); }
  .divider-gold-shine { background: linear-gradient(90deg, var(--gold) 0%, var(--gold) 45%, #ffffff 55%, var(--gold) 65%, var(--gold) 100%); }

  .contact-block {
    position: absolute; left: 0; width: 100%; top: 150px;
    text-align: center; color: var(--white);
  }
  .contact-name { font-size: 18px; font-weight: 400; color: var(--gold); line-height: 24px; }
  .contact-line {
    font-size: 12px; line-height: 19px; margin-top: 2px;
    display: flex; justify-content: center; align-items: center; gap: 3px;
  }
  .contact-line + .contact-line { margin-top: 0; }
  .contact-line svg { display: block; }
</style>
</head>
<body>

  <!-- Row 1 -->
  <section class="card card-front" style="top:2px;">
    <div class="damask-fill" role="img" aria-label="Dark damask ornament pattern background"></div>
    <div class="brand-name brand-gold"><span class="wordmark">quarry5</span><span class="tagline">business collective</span></div>
    <div class="band-long band-gold-glow"></div>
    <span class="web-address">www. quarry-5.com</span>
    <div class="band-short band-gold-glow-short"></div>
  </section>
  <section class="card card-back" style="top:6px;">
    <div class="damask-fill" role="img" aria-label="Dark damask ornament pattern background"></div>
    <h2 class="company-heading">QUARRY5 BUSINESS COLLECTIVE</h2>
    <div class="divider divider-gold-fade"></div>
    <div class="contact-block">
      <p class="contact-name">LENA MOOR</p>
      <p class="contact-line"><svg width="6" height="10" viewBox="0 0 6 10"><rect x="0.5" y="0.5" width="5" height="9" rx="1" fill="none" stroke="#f6c231"/></svg>+34 611 204 587</p>
      <p class="contact-line"><svg width="11" height="8" viewBox="0 0 11 8"><rect x="0.5" y="0.5" width="10" height="7" fill="none" stroke="#f6c231"/><path d="M0.5 0.5 L5.5 4.5 L10.5 0.5" fill="none" stroke="#f6c231"/></svg>info@quarry-5.com</p>
    </div>
  </section>

  <!-- Row 2 -->
  <section class="card card-front" style="top:253px;">
    <div class="damask-fill" role="img" aria-label="Dark damask ornament pattern background"></div>
    <div class="brand-name brand-silver"><span class="wordmark">quarry5</span><span class="tagline">business collective</span></div>
    <div class="band-long band-silver"></div>
    <span class="web-address gold">www. quarry-5.com</span>
    <div class="band-short band-silver-short"></div>
  </section>
  <section class="card card-back" style="top:257px;">
    <div class="damask-fill" role="img" aria-label="Dark damask ornament pattern background"></div>
    <h2 class="company-heading gold">QUARRY5 BUSINESS COLLECTIVE</h2>
    <div class="divider divider-silver"></div>
    <div class="contact-block">
      <p class="contact-name">LENA MOOR</p>
      <p class="contact-line"><svg width="6" height="10" viewBox="0 0 6 10"><rect x="0.5" y="0.5" width="5" height="9" rx="1" fill="none" stroke="#f6c231"/></svg>+34 611 204 587</p>
      <p class="contact-line"><svg width="11" height="8" viewBox="0 0 11 8"><rect x="0.5" y="0.5" width="10" height="7" fill="none" stroke="#f6c231"/><path d="M0.5 0.5 L5.5 4.5 L10.5 0.5" fill="none" stroke="#f6c231"/></svg>info@quarry-5.com</p>
    </div>
  </section>

  <!-- Row 3 -->
  <section class="card card-front" style="top:503px;">
    <div class="damask-fill" role="img" aria-label="Dark damask ornament pattern background"></div>
    <div class="brand-name brand-gold"><span class="wordmark">quarry5</span><span class="tagline">business collective</span></div>
    <div class="band-long band-gold-flat"></div>
    <span class="web-address">www. quarry-5.com</span>
    <div class="band-short band-gold-flat"></div>
  </section>
  <section class="card card-back" style="top:507px;">
    <div class="damask-fill" role="img" aria-label="Dark damask ornament pattern background"></div>
    <h2 class="company-heading">QUARRY5 BUSINESS COLLECTIVE</h2>
    <div class="divider divider-gold-flat"></div>
    <div class="contact-block">
      <p class="contact-name">LENA MOOR</p>
      <p class="contact-line"><svg width="6" height="10" viewBox="0 0 6 10"><rect x="0.5" y="0.5" width="5" height="9" rx="1" fill="none" stroke="#f6c231"/></svg>+34 611 204 587</p>
      <p class="contact-line"><svg width="11" height="8" viewBox="0 0 11 8"><rect x="0.5" y="0.5" width="10" height="7" fill="none" stroke="#f6c231"/><path d="M0.5 0.5 L5.5 4.5 L10.5 0.5" fill="none" stroke="#f6c231"/></svg>info@quarry-5.com</p>
    </div>
  </section>

  <!-- Row 4 -->
  <section class="card card-front" style="top:752px;">
    <div class="damask-fill" role="img" aria-label="Dark damask ornament pattern background"></div>
    <div class="brand-name brand-gold"><span class="wordmark">quarry5</span><span class="tagline">business collective</span></div>
    <div class="band-long band-gold-glow"></div>
    <span class="web-address">www. quarry-5.com</span>
    <div class="band-short band-gold-flat"></div>
  </section>
  <section class="card card-back" style="top:756px;">
    <div class="damask-fill" role="img" aria-label="Dark damask ornament pattern background"></div>
    <h2 class="company-heading">QUARRY5 BUSINESS COLLECTIVE</h2>
    <div class="divider divider-gold-shine"></div>
    <div class="contact-block">
      <p class="contact-name">LENA MOOR</p>
      <p class="contact-line"><svg width="6" height="10" viewBox="0 0 6 10"><rect x="0.5" y="0.5" width="5" height="9" rx="1" fill="none" stroke="#f6c231"/></svg>+34 611 204 587</p>
      <p class="contact-line"><svg width="11" height="8" viewBox="0 0 11 8"><rect x="0.5" y="0.5" width="10" height="7" fill="none" stroke="#f6c231"/><path d="M0.5 0.5 L5.5 4.5 L10.5 0.5" fill="none" stroke="#f6c231"/></svg>info@quarry-5.com</p>
    </div>
  </section>

</body>
</html>
```